Spa needs a highly desired Membership Card

We need a membership card that captures people's desire to own it(our membership) when flashed by anyone! It should tell the "class" of the card owner!
Comes in Silver & Gold membership. Wants to have same design in different colour/tone to differentiate Gold & Silver.
Most members are woman, but we have few men as well.
Updates
Hi Designers,
Target Market(s)
Woman age 25-55 years old. High spending power in a relatively poor country(Myanmar).
They may be rich businesswomen, wives/daughters of rich man, women who are educated abroad and now return to home country as Myanmar is fast developing.
Requirements
Must have
- Must be in tiff, bmp or jpeg format so that card printer can recognise.
- TEXT
- Velmora Spa (font: Monotype Corsiva)
- No 82, Kintha Street, Mawlin Plaza (Level-5) (7716), Sanchaung Township, Yangon
- 09 47283916
- contactus@tervane-holdco.example
- A space for picture of card owner.
- No magnetic strip/smart chip.
- Name Abcdefghijklmn
- Membership No 12345678
- Expiry MM/YYYY
- For Gold:
- Terms and Conditions
- - Members enjoy 25% off all standard services, excluding promotional offers
- - Members enjoy 5% off for Lumivessa products, excluding promotional items
- - Members enjoy 10% off for all other retail products, excluding promotional items
- - 1 accompanying guest in a day enjoys 20% off standard services, excluding promotional offers
- - Memberships are valid for 2 years from the date of issue and are non-transferable
- - Memberships sold are non-refundable or exchangeable for cash, services or products
- - Privileges are subject to change without prior notice
- For Silver:
- Terms and Conditions
- - Members enjoy 20% off all standard services, excluding promotional offers
- I uploaded 2 of our spa pictures so you can have a feel our of premise. And uploaded our name card, I agree its not stylish as I designed it myself.

```html
<!DOCTYPE html>
<html lang="en">
<head>
<meta charset="utf-8">
<title>Velmora Spa – Silver Membership Card</title>
<link rel="stylesheet" href="https://fonts.googleapis.com/css2?family=Cormorant+Garamond:wght@500;600&family=Quicksand:wght@600;700&display=swap">
<style>
  :root {
    --page: #ffffff;
    --card: #000000;
    --silver: #d4d4d4;
    --silver-light: #f2f2f2;
    --silver-dark: #8a8a8a;
    --ink: #ffffff;
    --photo: #ffffff;
    --photo-shade: #e6e6e6;
  }
  * { box-sizing: border-box; margin: 0; padding: 0; }
  html, body {
    width: 967px; height: 1200px; overflow: hidden;
    background: var(--page);
  }
  .card {
    position: absolute; left: 67px; width: 838px; height: 527px;
    background: var(--card); border-radius: 46px;
    box-shadow: 0 8px 22px rgba(0,0,0,0.18);
    overflow: hidden;
  }
  .card--front { top: 47px; }
  .card--back { top: 616px; }

  .brand-name {
    position: absolute; left: 0; right: 0; text-align: center;
    font-family: "Cormorant Garamond", Georgia, serif; font-weight: 600;
    color: var(--silver); letter-spacing: 1px; white-space: nowrap;
  }
  .card--front .brand-name { top: 156px; font-size: 62px; line-height: 1; }

  .ornament {
    position: absolute; left: 309px; width: 210px; border-radius: 40px;
    background: radial-gradient(ellipse at center, var(--silver-light) 0%, var(--silver-dark) 55%, rgba(0,0,0,0) 78%);
    opacity: 0.85;
  }
  .ornament--top { top: 243px; height: 78px; }
  .ornament--bottom { top: 396px; height: 82px; }

  .tier-rule {
    position: absolute; left: 121px; width: 591px; height: 3px;
    background: var(--silver);
  }
  .tier-rule--top { top: 327px; }
  .tier-rule--bottom { top: 392px; }
  .tier-title {
    position: absolute; left: 121px; width: 591px; top: 332px;
    text-align: center; font-family: "Cormorant Garamond", Georgia, serif;
    font-weight: 500; font-size: 59px; line-height: 58px; color: var(--silver);
    letter-spacing: 0.5px; white-space: nowrap;
  }

  .card--back .brand-name { left: 52px; right: auto; width: 300px; top: 102px; font-size: 44px; line-height: 1; }

  .member-photo {
    position: absolute; left: 123px; top: 175px; width: 166px; height: 166px;
    background: linear-gradient(180deg, var(--photo) 0%, var(--photo-shade) 100%);
  }
  .member-name {
    position: absolute; left: 76px; width: 260px; top: 358px; text-align: center;
    font-family: "Quicksand", Arial, sans-serif; font-weight: 700;
    font-size: 30px; color: var(--ink); letter-spacing: 0.5px; white-space: nowrap;
  }
  .contact-block {
    position: absolute; right: 33px; top: 26px; text-align: right;
    font-family: "Quicksand", Arial, sans-serif; font-weight: 700;
    font-size: 27px; line-height: 30px; color: var(--ink);
    letter-spacing: 0.8px; white-space: nowrap;
  }
  .validity {
    position: absolute; top: 240px;
    font-family: "Quicksand", Arial, sans-serif; font-weight: 700;
    font-size: 26px; line-height: 29.5px; color: var(--ink);
    letter-spacing: 1px; white-space: nowrap;
  }
  .validity--from { left: 425px; }
  .validity--until { left: 635px; }
  .address {
    position: absolute; left: 51px; top: 472px;
    font-family: "Quicksand", Arial, sans-serif; font-weight: 700;
    font-size: 15px; line-height: 21px; color: var(--ink); white-space: nowrap;
  }
</style>
</head>
<body>
  <section class="card card--front">
    <div class="brand-name">Velmora Spa</div>
    <div class="ornament ornament--top" role="img" aria-label="Silver scroll ornament above the tier title"></div>
    <div class="tier-rule tier-rule--top"></div>
    <h1 class="tier-title">SILVER MEMBERSHIP</h1>
    <div class="tier-rule tier-rule--bottom"></div>
    <div class="ornament ornament--bottom" role="img" aria-label="Silver scroll ornament below the tier title"></div>
  </section>

  <section class="card card--back">
    <div class="brand-name">Velmora Spa</div>
    <div class="contact-block">
      <div>Aren Soe Lwin</div>
      <div>Director</div>
      <div>(959) 482106653 (YGN)</div>
      <div>(65) 91730486 (SGP)</div>
    </div>
    <div class="member-photo" role="img" aria-label="Space for the card owner's photograph"></div>
    <div class="member-name">NAME NAME</div>
    <div class="validity validity--from">VALID<br>FROM &gt;<br>00/00/00</div>
    <div class="validity validity--until">EXPIRES<br>END &gt;<br>00/00/00</div>
    <p class="address">No 82, Kintha Street, Mawlin Plaza (Level-5) (7716),<br>Sanchaung Township, Yangon. // T : 09 47283916 // E : contactus@tervane-holdco.example</p>
  </section>
</body>
</html>
```